A layout of a webpage for oil trade platform

I would like to have a desgin of one page webpage (with section scrollling dowin) that woulf present the new product i.e. oil trade platform for wholesale buyers and sellers.
Layout should consist of the sections similar to the given at: https://strona.trawomirek.pl/modul-planowania-spotkan
However oil industy require more colors and more photo stories than here for doctor.
I. I woul imagine at first below menu a slider with brueg information about the product and its advantages with "more" button next to the prict screen of our platform on different displays (PC and mobile).
II. Bellow the slider I would imagine icons correspoing to the advantages of that plaftorm:
1. Purchase/sale process automation 24/7
2. Access to the best deals
3. Electronic offerings and orderings
4. Transaction status monitoring
5. Data and transaction security
II A) (optional):
In near future we would like to prepare a short video presenation. Hence please prepare a place to display that element here.
At the moment alternatvily please prepare a How it works section that would explan the platform operating process
III. Next secion is about benefits for Oil Purchaser
It can be done either by icons of by text and corresponding grahip for while section.
Benefits:
- Access to cheaper oil
- Convenience of online orders
- Possibility to compare prices on the market
- Transaction history
- Order status monitoring
- Seccurity and transparency of purchase
IV. Next seciont is about benefits for Oil Seller
Benefits:
- New sale channel
- Attracting new clients
- More oil sold
- Transaction security
- Possibility to integrate with distribution infrastructure and logistits for more efficient automation.
V. Contact form
VI. Footer
I would need a layout that that will correspond to the very dynamic logo but I would expect also a clean form, smoth and modern. It has to be proffessional layout with more corporate character.
It can use a paralax features if needed.
Attachments:
- logo design
- platfrom print screen
Industry/Entity Type
Oil And Gas
Number of Pages Required
1 page

```html
<!DOCTYPE html>
<html lang="en">
<head>
<meta charset="utf-8">
<title>Crudelink — Oil trade platform</title>
<link href="https://fonts.googleapis.com/css2?family=Roboto:wght@300;400;500;700&display=swap" rel="stylesheet">
<style>
:root{
  --orange:#f36a21;
  --orange-light:#fb9a3e;
  --navy:#0f1f3d;
  --hero-a:#44516b;
  --hero-b:#2d3850;
  --green-a:#5cb531;
  --green-b:#3f8a1c;
  --ink:#333a44;
  --muted:#6d737b;
  --icon:#5a6270;
  --white:#fff;
}
*{box-sizing:border-box;margin:0;padding:0}
html,body{width:1200px;height:3046px;overflow:hidden}
body{font-family:'Roboto',sans-serif;color:var(--ink);background:var(--white);position:relative}
.abs{position:absolute}

/* nav */
.nav{top:0;left:0;width:1200px;height:60px;background:var(--white)}
.brand{left:88px;top:16px;display:flex;align-items:center;gap:8px;font-size:19px;font-weight:700;color:var(--navy)}
.brand-dot{width:20px;height:20px;border-radius:50%;background:var(--orange)}
.menu{right:108px;top:22px;display:flex;gap:34px;font-size:13.5px;color:#333}
.menu .active{color:var(--orange)}

/* hero */
.hero{top:60px;left:0;width:1200px;height:557px;background:linear-gradient(180deg,var(--hero-a),var(--hero-b))}
.tag{left:88px;top:268px;background:var(--orange);color:var(--white);font-size:13px;padding:7px 10px}
.hero-title{left:88px;top:306px;font-size:32px;font-weight:400;color:var(--white)}
.hero-text{left:88px;top:360px;width:440px;font-size:13px;line-height:17px;color:#e6e9ef}
.btn-more{left:88px;top:420px;width:96px;height:36px;border-radius:18px;background:var(--orange);color:var(--white);font-size:13px;display:flex;align-items:center;justify-content:center;gap:6px}
.hero-devices{left:700px;top:180px;width:500px;height:365px;background:linear-gradient(160deg,#dfe3ea,#9aa4b5);border-radius:10px 0 0 10px}
.scroll-mouse{left:590px;top:558px;width:20px;height:32px;border:2px solid #fff;border-radius:10px}
.scroll-mouse::after{content:"";position:absolute;left:7px;top:6px;width:2px;height:7px;background:#fff;border-radius:1px}

/* features */
.feature{top:735px;width:200px;text-align:center;font-size:13px;line-height:18px;color:var(--ink)}
.feature svg{display:block;margin:0 auto 14px}

/* how it works */
.how-media{left:88px;top:940px;width:447px;height:283px;background:linear-gradient(135deg,#b8b3ac,#6e6c6a)}
.play{left:285px;top:1060px;width:52px;height:52px;border-radius:50%;background:var(--white);display:flex;align-items:center;justify-content:center}
.section-title{font-size:30px;font-weight:300;color:var(--ink)}
.how-title{left:615px;top:990px}
.how-text{left:615px;top:1040px;width:500px;font-size:13px;line-height:19px;color:var(--muted)}
.how-text p+p{margin-top:10px}

/* purchaser */
.purchaser{top:1315px;left:0;width:1200px;height:507px;background:linear-gradient(90deg,var(--green-a),var(--green-b));overflow:hidden;color:var(--white)}
.purchaser-title{left:0;width:1200px;top:80px;text-align:center;font-size:30px;font-weight:300}
.benefit-label{font-size:13px;line-height:18px}
.benefit-label.right{text-align:right}

/* seller */
.seller-devices{left:0;top:1935px;width:455px;height:300px;background:linear-gradient(150deg,#e2e6ec,#8f98a6)}
.seller-title{left:572px;top:1965px}
.seller-list{left:572px;top:2022px;width:440px;list-style:none;font-size:13px;color:var(--ink)}
.seller-list li{display:flex;align-items:flex-start;gap:12px;height:42px;line-height:18px}
.seller-list svg{flex:none}

/* contact */
.contact{top:2343px;left:0;width:1200px;height:405px;background:linear-gradient(90deg,#f05a22,#fb8c33)}
.contact-title{left:0;width:1200px;top:70px;text-align:center;color:var(--white);font-size:30px;font-weight:300}
.field{background:var(--white);border-radius:22px;font-size:13px;color:#777;padding:0 20px;display:flex;align-items:center}
.field.input{left:158px;width:432px;height:44px}
.field.message{left:605px;top:127px;width:437px;height:160px;border-radius:20px;align-items:flex-start;padding-top:16px}
.btn-send{left:520px;top:305px;width:160px;height:38px;border-radius:19px;background:var(--orange-light);color:var(--white);font-size:13px;display:flex;align-items:center;justify-content:center}

/* footer */
.footer{top:2748px;left:0;width:1200px;height:298px;background:var(--navy);color:var(--white)}
.col{top:96px;width:230px;font-size:12.5px;line-height:25px}
.col h4{font-size:14px;font-weight:700;margin-bottom:6px}
.col b{font-weight:700}
.rule{left:88px;top:247px;width:1024px;height:1px;background:#25365a}
.copyright{left:0;width:1200px;top:264px;text-align:center;font-size:12px}
.to-top{left:1112px;top:230px;width:38px;height:38px;border-radius:50%;background:var(--orange);display:flex;align-items:center;justify-content:center}
</style>
</head>
<body>

<header class="abs nav">
  <div class="abs brand"><span class="brand-dot"></span>Crudelink</div>
  <nav class="abs menu">
    <span class="active">&#8962; Home</span><span>Advantages</span><span>How It Works</span><span>Benefits</span><span>Contact</span>
  </nav>
</header>

<section class="abs hero">
  <div class="abs tag" style="top:208px">Oil trade platform for</div>
  <h1 class="abs hero-title" style="top:246px">Wholesale buyers and sellers</h1>
  <p class="abs hero-text" style="top:296px">Lorem ipsum dolor sit amet, consectetuer adipiscing elit. Aenean commodo ligula eget dolor. Aenean massa. Cum sociis natoque penatibus et magnis dis parturient montes, nascetur ridiculus mus.</p>
  <div class="abs btn-more" style="top:356px">More <span>&#8594;</span></div>
  <div class="abs hero-devices" style="top:120px" role="img" aria-label="Platform dashboard shown on a laptop and a phone"></div>
  <div class="abs scroll-mouse" style="top:498px"></div>
</section>

<section id="advantages">
  <div class="abs feature" style="left:68px">
    <svg width="52" height="52" viewBox="0 0 52 52" fill="none" stroke="var(--icon)" stroke-width="1.6"><path d="M8 26a18 18 0 1 0 6-13"/><path d="M8 8v8h8"/><text x="26" y="31" font-size="13" text-anchor="middle" fill="var(--icon)" stroke="none" font-family="Roboto">24</text></svg>
    Purchase/sale process<br>automation 24/7
  </div>
  <div class="abs feature" style="left:294px">
    <svg width="52" height="52" viewBox="0 0 52 52" fill="none" stroke="var(--icon)" stroke-width="1.6"><rect x="6" y="22" width="10" height="22"/><path d="M16 24l8-14c4 0 5 3 4 8h12c3 0 4 3 3 6l-4 14c-1 3-3 4-6 4H16"/></svg>
    Access to the best<br>deals
  </div>
  <div class="abs feature" style="left:519px">
    <svg width="52" height="52" viewBox="0 0 52 52" fill="none" stroke="var(--orange)" stroke-width="1.6"><rect x="13" y="13" width="26" height="26"/><rect x="19" y="19" width="14" height="14"/><path d="M19 7v6M26 7v6M33 7v6M19 39v6M26 39v6M33 39v6M7 19h6M7 26h6M7 33h6M39 19h6M39 26h6M39 33h6"/></svg>
    Electronic offerings<br>and orderings
  </div>
  <div class="abs feature" style="left:726px">
    <svg width="52" height="52" viewBox="0 0 52 52" fill="none" stroke="var(--icon)" stroke-width="1.6"><rect x="5" y="8" width="42" height="30"/><path d="M26 38v6M16 45h20M11 30l9-9 7 6 12-12"/></svg>
    Transaction status<br>monitoring
  </div>
  <div class="abs feature" style="left:935px">
    <svg width="52" height="52" viewBox="0 0 52 52" fill="none" stroke="var(--icon)" stroke-width="1.6"><ellipse cx="22" cy="10" rx="14" ry="5"/><path d="M8 10v28c0 3 6 5 14 5M36 10v14M8 19c0 3 6 5 14 5s14-2 14-5M8 28c0 3 6 5 14 5"/><rect x="30" y="32" width="14" height="11"/><path d="M33 32v-4a4 4 0 0 1 8 0v4"/></svg>
    Data and transaction<br>security
  </div>
</section>

<section id="how-it-works">
  <div class="abs how-media" role="img" aria-label="Video preview: person checking the platform on a smartphone"></div>
  <div class="abs play"><svg width="18" height="20" viewBox="0 0 18 20"><path d="M2 1l15 9-15 9z" fill="var(--orange)"/></svg></div>
  <h2 class="abs section-title how-title">How It Works</h2>
  <div class="abs how-text">
    <p>Lorem ipsum dolor sit amet, consectetuer adipiscing elit. Aenean commodo ligula eget dolor. Cum sociis natoque penatibus et magnis dis parturient montes, nascetur ridiculus mus. Donec quam felis, ultricies nec, pellentesque eu, pretium quis, sem. Nulla consequat massa quis enim.</p>
    <p>Cum sociis natoque penatibus et magnis dis parturient montes, nascetur ridiculus mus. Donec quam felis, ultricies nec, pellentesque eu, pretium quis, sem. Nulla consequat massa quis enim.</p>
  </div>
</section>

<section class="abs purchaser" id="benefits">
  <h2 class="abs purchaser-title">Benefits for Oil Purchaser</h2>
  <svg class="abs" style="left:0;top:0" width="1200" height="507" viewBox="0 0 1200 507">
    <circle cx="600" cy="511" r="238" fill="none" stroke="#fff" stroke-width="2"/>
    <circle cx="600" cy="511" r="150" fill="rgba(255,255,255,0.18)"/>
    <circle cx="600" cy="511" r="120" fill="#fff"/>
    <text x="600" y="468" text-anchor="middle" font-family="Roboto,sans-serif" font-size="22" font-weight="700" fill="#0f1f3d">Crudelink</text>
    <g fill="#fff">
      <circle cx="527" cy="281" r="6"/><circle cx="673" cy="281" r="6"/>
      <circle cx="432" cy="340" r="6"/><circle cx="768" cy="340" r="6"/>
      <circle cx="404" cy="392" r="6"/><circle cx="796" cy="392" r="6"/>
    </g>
    <g stroke="#fff" stroke-width="1.5" fill="none">
      <line x1="527" y1="281" x2="481" y2="222"/><line x1="673" y1="281" x2="708" y2="222"/>
      <line x1="432" y1="340" x2="366" y2="305"/><line x1="768" y1="340" x2="824" y2="300"/>
      <line x1="404" y1="392" x2="284" y2="413"/><line x1="796" y1="392" x2="889" y2="407"/>
    </g>
    <g fill="#fff" stroke="rgba(255,255,255,0.45)" stroke-width="6">
      <circle cx="481" cy="196" r="38"/><circle cx="708" cy="196" r="38"/>
      <circle cx="363" cy="281" r="38"/><circle cx="824" cy="281" r="38"/>
      <circle cx="284" cy="413" r="38"/><circle cx="889" cy="407" r="38"/>
    </g>
    <g fill="none" stroke="#555" stroke-width="1.6">
      <rect x="468" y="188" width="20" height="18"/><path d="M488 194l8-4v14"/>
      <circle cx="708" cy="196" r="13"/><path d="M708 188v8l6 4"/>
      <rect x="350" y="271" width="26" height="18"/><path d="M363 289v5M356 294h14M357 281l4 3 6-7"/>
      <rect x="811" y="271" width="26" height="18"/><path d="M815 285l6-6 4 3 7-7"/>
      <rect x="271" y="404" width="26" height="16"/><path d="M284 420v6M276 412l5 3 5-4 6 3"/>
      <path d="M882 396h14v26h-14zM886 396v-5h6v5M884 410h10"/>
    </g>
  </svg>
  <div class="abs benefit-label right" style="left:300px;width:124px;top:178px">Access<br>to cheaper oil</div>
  <div class="abs benefit-label" style="left:778px;top:178px">Transaction<br>history</div>
  <div class="abs benefit-label right" style="left:176px;width:122px;top:263px">Convenience of<br>online orders</div>
  <div class="abs benefit-label" style="left:888px;top:263px">Order status<br>monitoring</div>
  <div class="abs benefit-label right" style="left:60px;width:166px;top:394px">Possibility to compare<br>priceson the market</div>
  <div class="abs benefit-label" style="left:952px;top:394px">Security and transparency<br>of purchase</div>
</section>

<section id="seller">
  <div class="abs seller-devices" role="img" aria-label="Platform dashboard shown on desktop, laptop, tablet and phone"></div>
  <h2 class="abs section-title seller-title">Benefits for Oil Seller</h2>
  <ul class="abs seller-list">
    <li><svg width="18" height="18" viewBox="0 0 18 18" fill="none" stroke="var(--icon)" stroke-width="1.3"><circle cx="9" cy="9" r="2.5"/><circle cx="3" cy="3" r="2"/><circle cx="15" cy="3" r="2"/><circle cx="3" cy="15" r="2"/><circle cx="15" cy="15" r="2"/><path d="M5 5l2 2M13 5l-2 2M5 13l2-2M13 13l-2-2"/></svg>New sale channel</li>
    <li><svg width="18" height="18" viewBox="0 0 18 18" fill="none" stroke="var(--icon)" stroke-width="1.3"><circle cx="9" cy="6" r="4"/><path d="M1.5 17c1-4 4-6 7.5-6s6.5 2 7.5 6"/></svg>Attracting new clients</li>
    <li><svg width="18" height="18" viewBox="0 0 18 18" fill="none" stroke="var(--icon)" stroke-width="1.3"><path d="M4 5h10v12H4zM7 5V2h4v3M6 11h6"/></svg>More oil sold</li>
    <li><svg width="18" height="18" viewBox="0 0 18 18" fill="none" stroke="var(--icon)" stroke-width="1.3"><rect x="3" y="8" width="12" height="9"/><path d="M5.5 8V5a3.5 3.5 0 0 1 7 0v3"/></svg>Transaction security</li>
    <li><svg width="18" height="18" viewBox="0 0 18 18" fill="none" stroke="var(--icon)" stroke-width="1.3"><path d="M9 1l7 3v5c0 4-3 7-7 8-4-1-7-4-7-8V4z"/><circle cx="9" cy="9" r="2.5"/></svg>Possibility to integrate with distribution infrastructure and<br>logistits for more efficient automation.</li>
  </ul>
</section>

<section class="abs contact" id="contact">
  <h2 class="abs contact-title">Contact Us</h2>
  <div class="abs field input" style="top:127px">Name*</div>
  <div class="abs field input" style="top:179px">Email*</div>
  <div class="abs field input" style="top:231px">Phone*</div>
  <div class="abs field message">Message*</div>
  <div class="abs btn-send">Send Message</div>
</section>

<footer class="abs footer">
  <div class="abs col" style="left:176px"><h4>Office address</h4>58 Refinery Row<br>Harbor Flats, TX 7702</div>
  <div class="abs col" style="left:436px"><h4>Get in touch</h4><b>Tel:</b> +0 555-210-4431<br><b>Fax:</b> +0 555-210-4432<br><b>Email:</b> hello@crudelink-mail.test</div>
  <div class="abs col" style="left:696px"><h4>Website info</h4>Terms and Conditions<br>Privacy Policy<br>Acceptable Use Policy</div>
  <div class="abs col" style="left:956px"><h4>Social media</h4>Community<br>Updates<br>Gallery</div>
  <div class="abs rule"></div>
  <div class="abs copyright">Copyright 2017 Crudelink | All Right Reserved</div>
  <div class="abs to-top"><svg width="12" height="8" viewBox="0 0 12 8"><path d="M1 7l5-5 5 5" fill="none" stroke="#fff" stroke-width="2"/></svg></div>
</footer>

</body>
</html>
```